Vellandor Insurance & Consulting

We need a new business card designed.
Front Side:
Photo on left
Logo on top right
Name, title, company, and contact info aligned on right
Clean spacing with professional hierarchy

Back Side:
Tagline centered near the top:
Real expertise. Practical guidance. Reliable protection.

Coverage types centered below in 2 lines:
General Liability | Workers Comp | Commercial Auto
Property | Inland Marine | Excess Liability | Pollution

```html
<!DOCTYPE html>
<html lang="en">
<head>
<meta charset="utf-8">
<title>Vellandor Insurance &amp; Consulting – Business Card</title>
<link href="https://fonts.googleapis.com/css2?family=Poppins:wght@400;500;700&display=swap" rel="stylesheet">
<style>
  :root {
    --page: #262627;
    --card: #2b2a2d;
    --ink-light: #ffffff;
    --ink-dark: #1e1e20;
    --band: #ffffff;
    --photo-a: #c9c7c6;
    --photo-b: #6b5448;
  }
  * { box-sizing: border-box; margin: 0; padding: 0; }
  html, body { width: 1200px; height: 800px; overflow: hidden; }
  body {
    background: var(--page);
    font-family: "Poppins", sans-serif;
    color: var(--ink-light);
    position: relative;
  }
  .card {
    position: absolute;
    width: 540px;
    height: 310px;
    background: var(--card);
    border-radius: 26px;
    overflow: hidden;
  }
  .card--back { left: 40px; top: 245px; }
  .card--front { left: 620px; top: 245px; }

  /* Back side */
  .tagline {
    position: absolute; top: 34px; left: 0; right: 0;
    text-align: center; font-size: 13px; letter-spacing: 0.3px;
  }
  .brand {
    position: absolute; top: 108px; left: 0; right: 0;
    display: flex; align-items: center; justify-content: center; gap: 12px;
  }
  .brand__dot {
    width: 26px; height: 26px; border-radius: 50%; background: var(--ink-light);
  }
  .brand__name { font-size: 22px; font-weight: 500; line-height: 1.15; }
  .coverage {
    position: absolute; top: 212px; left: 0; right: 0;
    text-align: center; font-size: 14px; line-height: 1.55;
  }

  /* Front side */
  .brand--front {
    top: 36px; left: auto; right: 28px; justify-content: flex-end; gap: 10px;
  }
  .brand--front .brand__name { font-size: 17px; text-align: right; }
  .brand--front .brand__dot { width: 22px; height: 22px; }
  .name-band {
    position: absolute; left: 0; right: 0; top: 112px; height: 56px;
    background: var(--band); color: var(--ink-dark);
    text-align: right; padding-right: 28px; padding-top: 5px;
  }
  .name-band__name { font-size: 22px; font-weight: 700; line-height: 1.2; }
  .name-band__title { font-size: 12px; font-weight: 500; line-height: 1.2; }
  .photo {
    position: absolute; left: 34px; top: 56px;
    width: 172px; height: 172px; border-radius: 50%;
    border: 5px solid var(--band);
    background: radial-gradient(circle at 45% 40%, var(--photo-b) 0 28%, var(--photo-a) 60%);
  }
  .contact {
    position: absolute; right: 28px; top: 182px;
    text-align: right; font-size: 11.5px; line-height: 1.6;
  }
  .contact__row { display: flex; justify-content: flex-end; align-items: center; gap: 8px; }
  .icon { width: 14px; height: 14px; flex: none; }
  .icon--blank { visibility: hidden; }
</style>
</head>
<body>

<section class="card card--back" aria-label="Card back">
  <p class="tagline">• Real expertise • Practical guidance • Reliable protection</p>
  <div class="brand">
    <span class="brand__dot"></span>
    <span class="brand__name">Vellandor<br>Insurance &amp; Consulting</span>
  </div>
  <p class="coverage">
    General Liability | Workers Comp | Commercial Auto<br>
    Property | Inland Marine | Excess Liability | Pollution
  </p>
</section>

<section class="card card--front" aria-label="Card front">
  <div class="name-band">
    <p class="name-band__name">Marisol Vantreau</p>
    <p class="name-band__title">Agency Principal</p>
  </div>
  <div class="photo" role="img" aria-label="Portrait photo of the agency principal"></div>
  <div class="brand brand--front">
    <span class="brand__dot"></span>
    <span class="brand__name">Vellandor<br>Insurance &amp; Consulting</span>
  </div>
  <div class="contact">
    <div class="contact__row">Brightpath Insurance<svg class="icon icon--blank" viewBox="0 0 14 14"></svg></div>
    <div class="contact__row">(503) 555-0147
      <svg class="icon" viewBox="0 0 14 14"><rect width="14" height="14" rx="2" fill="#fff"/><path d="M4 3.5l1.6-.5 1 2-1 .8a5 5 0 0 0 2.6 2.6l.8-1 2 1-.5 1.6C7.5 10.6 3.4 6.5 4 3.5z" fill="#2b2a2d"/></svg>
    </div>
    <div class="contact__row">admin@brightpathins.com<svg class="icon icon--blank" viewBox="0 0 14 14"></svg></div>
    <div class="contact__row">www.vellandorinsurance.com
      <svg class="icon" viewBox="0 0 14 14"><rect width="14" height="14" rx="2" fill="#fff"/><circle cx="7" cy="7" r="4" fill="none" stroke="#2b2a2d" stroke-width="1.2"/><path d="M3 7h8M7 3c-2 2.5-2 5.5 0 8M7 3c2 2.5 2 5.5 0 8" fill="none" stroke="#2b2a2d" stroke-width="0.9"/></svg>
    </div>
    <div class="contact__row">1420 NW Alder Ave, Suite 310, Portland OR 97209
      <svg class="icon" viewBox="0 0 14 14"><rect width="14" height="14" rx="2" fill="#fff"/><path d="M7 12s-3.5-3.6-3.5-6a3.5 3.5 0 0 1 7 0C10.5 8.4 7 12 7 12z" fill="#2b2a2d"/><circle cx="7" cy="6" r="1.3" fill="#fff"/></svg>
    </div>
  </div>
</section>

</body>
</html>
```